BRAVEN POWERLINE SERVICES needs a vibrant design for electrical contracting work.

I require a card design for my own electrical contracting business. I will be doing a lot of domestic and commercial work, including things such as repairs, maintenance, lighting, installations and various others. LED lighting and energy efficiency will be a big part of my business. I wish not to have childish pictures such as light bulbs in the design, but rather a smart and modern looking card which incorporates my logo colours and perhaps the same lighting strike within the faded background of the card.

Target Market(s)

Residential and Commercial property owners.

Industry/Entity Type

Electrical

Contact Information for Business Card

Dalen Voskic
EC40923
Phone Number: 0417 358 942
Email: dalen@bravenpowerline.com

Font styles to use
Serif
Sans Serif

Requirements
Must have
• My Logo and associated colours.
Nice to have
• Some form of shapes splitting the card into different colours related to the colours of my logo. Electric Blue, Silver/Grey and White.
Should not have
• Childish pictures and symbols such as light bulbs.

```html
<!DOCTYPE html>
<html lang="en">
<head>
<meta charset="utf-8">
<title>Braven Powerline Services – Business Card</title>
<link rel="stylesheet" href="https://fonts.googleapis.com/css2?family=Saira:wght@400;500;600&display=swap">
<style>
  :root {
    --page: #e9e7e3;
    --card: #ffffff;
    --card-fade: #eef0f3;
    --electric-blue: #3d63c4;
    --electric-blue-light: #4f7bd6;
    --silver: #c9ccd1;
    --silver-dark: #9fa3a9;
    --grey: #a7a9ad;
    --grey-light: #c6c7ca;
    --ink-blue: #3b5fc0;
    --white: #ffffff;
  }
  html, body {
    margin: 0;
    width: 1200px;
    height: 1023px;
    overflow: hidden;
    background: var(--page);
    font-family: "Saira", sans-serif;
  }
  .card {
    position: absolute;
    left: 100px;
    top: 226px;
    width: 1000px;
    height: 572px;
    border-radius: 46px;
    overflow: hidden;
    background: linear-gradient(135deg, var(--card) 55%, var(--card-fade));
    box-shadow: 0 18px 40px rgba(0,0,0,0.18);
  }
  .card-shapes {
    position: absolute;
    inset: 0;
  }
  .brand {
    position: absolute;
    left: 70px;
    top: 62px;
    display: flex;
    align-items: center;
    gap: 22px;
    color: var(--ink-blue);
    font-weight: 600;
  }
  .brand-dot {
    width: 78px;
    height: 78px;
    border-radius: 50%;
    background: var(--ink-blue);
  }
  .brand-name {
    line-height: 0.95;
    letter-spacing: 1px;
  }
  .brand-name .primary { display: block; font-size: 66px; }
  .brand-name .secondary { display: block; font-size: 29px; letter-spacing: 2px; }
  .person {
    position: absolute;
    left: 300px;
    top: 262px;
    color: var(--ink-blue);
  }
  .person-name {
    font-size: 34px;
    font-weight: 500;
    letter-spacing: 1px;
  }
  .person-role {
    font-size: 22px;
    font-weight: 400;
    color: var(--ink-blue);
  }
  .person-role::before {
    content: "|";
    margin: 0 16px;
    font-size: 30px;
  }
  .person-licence {
    font-size: 22px;
    letter-spacing: 2px;
    margin-top: 2px;
  }
  .contact {
    position: absolute;
    left: 300px;
    top: 460px;
    list-style: none;
    margin: 0;
    padding: 0;
    color: var(--white);
    font-size: 22px;
    letter-spacing: 1px;
  }
  .contact li {
    display: flex;
    align-items: center;
    gap: 14px;
    height: 38px;
  }
  .contact-icon {
    width: 20px;
    height: 20px;
    border-radius: 4px;
    background: var(--white);
    display: flex;
    align-items: center;
    justify-content: center;
  }
</style>
</head>
<body>
  <section class="card" aria-label="Braven Powerline Services business card">
    <svg class="card-shapes" width="1000" height="572" viewBox="0 0 1000 572" aria-hidden="true">
      <defs>
        <linearGradient id="blue-band" x1="0" y1="0" x2="1" y2="1">
          <stop offset="0" stop-color="var(--electric-blue-light)"/>
          <stop offset="1" stop-color="var(--electric-blue)"/>
        </linearGradient>
        <linearGradient id="silver-edge" x1="0" y1="0" x2="1" y2="0">
          <stop offset="0" stop-color="#e6e8eb"/>
          <stop offset="0.5" stop-color="var(--silver-dark)"/>
          <stop offset="1" stop-color="#e6e8eb"/>
        </linearGradient>
      </defs>
      <!-- grey side panels -->
      <polygon class="grey-panel-light" points="700,0 1000,0 1000,572 820,572" fill="var(--grey-light)"/>
      <polygon class="grey-panel" points="800,0 1000,0 1000,572 900,572" fill="var(--grey)"/>
      <!-- silver edge above the blue band -->
      <polygon class="silver-edge" points="262,414 752,414 848,572 222,572" fill="url(#silver-edge)"/>
      <!-- electric blue contact band -->
      <polygon class="blue-band" points="272,428 744,428 832,572 234,572" fill="url(#blue-band)"/>
    </svg>

    <div class="brand">
      <span class="brand-dot" aria-hidden="true"></span>
      <span class="brand-name">
        <span class="primary">BRAVEN</span>
        <span class="secondary">POWERLINE SERVICES</span>
      </span>
    </div>

    <div class="person">
      <div><span class="person-name">Dalen Voskic</span><span class="person-role">Director</span></div>
      <div class="person-licence">EC40923</div>
    </div>

    <ul class="contact">
      <li>
        <span class="contact-icon" aria-hidden="true">
          <svg width="14" height="14" viewBox="0 0 14 14"><path d="M3 1.5l2 2.6-1.2 1.3c.8 1.8 2 3 3.8 3.8l1.3-1.2 2.6 2-1.3 2.3C5.6 12 2 8.4 1.7 2.8z" fill="var(--electric-blue)"/></svg>
        </span>
        0417 358 942
      </li>
      <li>
        <span class="contact-icon" aria-hidden="true">
          <svg width="14" height="14" viewBox="0 0 14 14"><rect x="1.5" y="3" width="11" height="8" fill="none" stroke="var(--electric-blue)" stroke-width="1.4"/><path d="M1.5 3.5L7 8l5.5-4.5" fill="none" stroke="var(--electric-blue)" stroke-width="1.4"/></svg>
        </span>
        dalen@bravenpowerline.com
      </li>
    </ul>
  </section>
</body>
</html>
```